Corbrook Estates LLC stationary for a real estate property management company.

Create stationary (letterhead, envelopes, business cards) using Corbrook Estates LLC logo as primary creative element. Stationary design needs to be horizontal, leaving as much space as possible for correspondence copy. See attached Creative Brief and past stationary files for details.

Target Market(s)

Prospective apartment residents and current residents, vendors, and government agencies.

Industry/Entity Type

Property Management

Contact Information for Business Card

Business card employee title: Property Manager. Should include address, phone, fax, email, website, slogan, and Corbrook Estates logo.

Font styles to use
Sans Serif

Colors
0592cd
000000

Requirements
Must have
• Tone should be conservative, institutional, business (i.e. banking, finance, real estate). Must include: address, phone, fax, website, and slogan (see attached Creative Brief). Should be a horizontal design, leaving as much room as possible for letter correspondence copy.
Nice to have
• Please use an Arial or Helvetica style font.
Should not have
• Letterhead layout should leave as much room as possible for copy.

```html
<!DOCTYPE html>
<html lang="en">
<head>
<meta charset="utf-8">
<title>Corbrook Estates LLC — Stationery</title>
<link rel="stylesheet" href="https://fonts.googleapis.com/css2?family=Arimo:wght@400;700&display=swap">
<style>
  :root {
    --board: #a87b52;
    --brand-blue: #1170b0;
    --charcoal: #454547;
    --paper: #ffffff;
    --arc-grey: #e6e7e8;
    --rule-grey: #e3e3e3;
    --muted: #777777;
    --shadow: 2px 3px 5px rgba(0,0,0,.35);
  }
  * { box-sizing: border-box; margin: 0; padding: 0; }
  html, body { width: 1200px; height: 770px; overflow: hidden; }
  body {
    position: relative;
    background: var(--board);
    font-family: "Arimo", Arial, sans-serif;
    color: var(--charcoal);
  }
  .sheet { position: absolute; background: var(--paper); box-shadow: var(--shadow); overflow: hidden; }

  /* brand lockup */
  .brand { position: absolute; display: flex; align-items: center; gap: 6px; color: var(--brand-blue); font-weight: 700; }
  .brand__mark { background: var(--brand-blue); flex: none; }
  .brand__name { display: flex; flex-direction: column; line-height: 1; }
  .brand__name .line1 { letter-spacing: .01em; }
  .brand__name .line2 { letter-spacing: .18em; }
  .brand--light { color: var(--paper); }
  .brand--light .brand__mark { background: var(--paper); }

  /* letterhead */
  .letterhead { left: 61px; top: 79px; width: 490px; height: 633px; }
  .letterhead__arc { position: absolute; left: 0; top: 0; }
  .letterhead .brand { left: 161px; top: 33px; }
  .letterhead .brand__mark { width: 28px; height: 34px; }
  .letterhead .line1 { font-size: 25px; }
  .letterhead .line2 { font-size: 10px; margin-top: 3px; }
  .footer { position: absolute; left: 0; right: 0; bottom: 0; background: var(--charcoal); color: var(--paper); }
  .footer svg { position: absolute; left: 0; top: 0; }
  .letterhead .footer { height: 57px; }
  .contact { position: absolute; font-size: 8px; line-height: 13px; }
  .contact .icon { color: var(--brand-blue); font-size: 7px; }
  .letterhead .contact { left: 30px; top: 25px; }
  .web { position: absolute; font-weight: 700; letter-spacing: .08em; font-size: 9px; }
  .letterhead .web { right: 34px; top: 32px; }

  /* business cards */
  .option-label { position: absolute; left: 678px; top: 182px; width: 200px; text-align: center; color: var(--paper); font-weight: 700; font-size: 13px; letter-spacing: .03em; }
  .card { top: 206px; width: 202px; height: 115px; }
  .card--front { left: 656px; }
  .card--back { left: 878px; background: var(--brand-blue); }
  .card__rule { position: absolute; left: 0; right: 0; top: 27px; height: 3px; background: var(--rule-grey); }
  .card--front .brand { right: 28px; top: 11px; background: var(--paper); padding: 0 4px; }
  .card .brand__mark { width: 12px; height: 15px; }
  .card .line1 { font-size: 11px; }
  .card .line2 { font-size: 4.5px; margin-top: 1px; }
  .card__person { position: absolute; right: 124px; top: 58px; text-align: right; }
  .card__name { color: var(--brand-blue); font-weight: 700; font-size: 7px; }
  .card__title { color: var(--muted); font-size: 5px; margin-top: 3px; }
  .card__divider { position: absolute; left: 88px; top: 57px; width: 1px; height: 42px; background: #cfcfcf; }
  .card__details { position: absolute; left: 99px; top: 58px; font-size: 4.3px; line-height: 6.4px; color: var(--muted); }
  .card__details .icon { color: var(--brand-blue); }
  .card__details .web { position: static; color: var(--brand-blue); font-size: 4.6px; letter-spacing: 0; margin-top: 3px; }
  .card--front .footer { height: 13px; }
  .card--back .brand { left: 52px; top: 40px; }
  .card--back .line1 { font-size: 13px; }
  .card--back .line2 { font-size: 5px; }
  .card--back .brand__mark { width: 14px; height: 18px; }

  /* envelope */
  .envelope-flap { position: absolute; left: 582px; top: 384px; }
  .flap-brand { position: absolute; left: 812px; top: 398px; transform: rotate(180deg); }
  .flap-brand .brand__mark { width: 14px; height: 18px; }
  .flap-brand .line1 { font-size: 13px; }
  .flap-brand .line2 { font-size: 5px; }
  .envelope { left: 582px; top: 458px; width: 560px; height: 252px; }
  .envelope .brand { left: 21px; top: 19px; }
  .envelope .brand__mark { width: 25px; height: 30px; }
  .envelope .line1 { font-size: 21px; }
  .envelope .line2 { font-size: 8.5px; margin-top: 2px; }
  .envelope .contact { left: 22px; top: 200px; color: var(--charcoal); }
  .envelope .web { right: 30px; top: 216px; color: var(--brand-blue); font-size: 8.5px; }
  .envelope .footer { height: 19px; }
</style>
</head>
<body>

  <!-- Letterhead -->
  <section class="sheet letterhead" aria-label="Letterhead">
    <svg class="letterhead__arc" width="220" height="210" viewBox="0 0 220 210" aria-hidden="true">
      <path d="M0 0 H190 C110 0 10 40 12 115 C13 160 40 190 60 206 C20 185 -5 150 0 100 Z" fill="var(--arc-grey)"/>
    </svg>
    <div class="brand">
      <span class="brand__mark"></span>
      <span class="brand__name"><span class="line1">CORBROOK</span><span class="line2">ESTATES LLC</span></span>
    </div>
    <footer class="footer">
      <svg width="490" height="8" viewBox="0 0 490 8" aria-hidden="true">
        <rect width="490" height="8" fill="var(--brand-blue)"/>
        <g fill="var(--charcoal)">
          <polygon points="40,0 77,0 85,8 48,8"/>
          <polygon points="126,0 163,0 171,8 134,8"/>
          <polygon points="212,0 249,0 257,8 220,8"/>
          <polygon points="298,0 335,0 343,8 306,8"/>
          <polygon points="384,0 421,0 429,8 392,8"/>
        </g>
      </svg>
      <div class="contact">
        2180 Alder Park Ave. #310, Riverton, CA 90412.<br>
        <span class="icon">&#9990;</span> 555-310-2748 &nbsp;<span class="icon">&#9632;</span> 555-310-2748
      </div>
      <div class="web">www.corbrookestates.us</div>
    </footer>
  </section>

  <!-- Business cards -->
  <div class="option-label">Front option 1</div>

  <section class="sheet card card--front" aria-label="Business card front">
    <div class="card__rule"></div>
    <div class="brand">
      <span class="brand__mark"></span>
      <span class="brand__name"><span class="line1">CORBROOK</span><span class="line2">ESTATES LLC</span></span>
    </div>
    <div class="card__person">
      <div class="card__name">Your Name Here</div>
      <div class="card__title">Designation</div>
    </div>
    <div class="card__divider"></div>
    <div class="card__details">
      2180 Alder Park Ave. #310,<br>
      Riverton, CA 90412.<br>
      <span class="icon">&#9990;</span> 555-310-2748<br>
      <span class="icon">&#9632;</span> 555-310-2748
      <div class="web">www.corbrookestates.us</div>
    </div>
    <footer class="footer">
      <svg width="202" height="4" viewBox="0 0 202 4" aria-hidden="true">
        <g fill="var(--brand-blue)">
          <polygon points="36,0 60,0 64,4 40,4"/>
          <polygon points="106,0 130,0 134,4 110,4"/>
          <polygon points="176,0 200,0 204,4 180,4"/>
        </g>
      </svg>
    </footer>
  </section>

  <section class="sheet card card--back" aria-label="Business card back">
    <div class="brand brand--light">
      <span class="brand__mark"></span>
      <span class="brand__name"><span class="line1">CORBROOK</span><span class="line2">ESTATES LLC</span></span>
    </div>
  </section>

  <!-- Envelope -->
  <svg class="envelope-flap" width="560" height="64" viewBox="0 0 560 64" aria-hidden="true">
    <path d="M0 64 L28 14 C34 4 40 0 55 0 H505 C520 0 526 4 532 14 L560 64 Z" fill="var(--brand-blue)" style="filter: drop-shadow(2px 3px 3px rgba(0,0,0,.3))"/>
  </svg>
  <div class="brand brand--light flap-brand">
    <span class="brand__mark"></span>
    <span class="brand__name"><span class="line1">CORBROOK</span><span class="line2">ESTATES LLC</span></span>
  </div>

  <section class="sheet envelope" aria-label="Envelope">
    <div class="brand">
      <span class="brand__mark"></span>
      <span class="brand__name"><span class="line1">CORBROOK</span><span class="line2">ESTATES LLC</span></span>
    </div>
    <div class="contact">
      2180 Alder Park Ave. #310, Riverton, CA 90412.<br>
      <span class="icon">&#9990;</span> 555-310-2748 &nbsp;<span class="icon">&#9632;</span> 555-310-2748
    </div>
    <div class="web">www.corbrookestates.us</div>
    <footer class="footer">
      <svg width="560" height="7" viewBox="0 0 560 7" aria-hidden="true">
        <g fill="var(--brand-blue)">
          <polygon points="0,0 42,0 48,7 0,7"/>
          <polygon points="94,0 136,0 142,7 100,7"/>
          <polygon points="188,0 230,0 236,7 194,7"/>
          <polygon points="282,0 324,0 330,7 288,7"/>
          <polygon points="376,0 418,0 424,7 382,7"/>
          <polygon points="470,0 512,0 518,7 476,7"/>
        </g>
      </svg>
    </footer>
  </section>

</body>
</html>
```